Visitenkarten-Design für Hausarztpraxis
Zielgruppe
Hausarztpraxis mit Schwerpunkt Geriatrie
Zielgruppe: Patienten in einem eher ländlichen Stadtgebiet mit hoher Anzahl von Senioren
Aufgabenstellung
Idee: Kombination eines Gutscheines für eine Kaffespezialität auf der Rückseite und einer beschreibbaren Vorderseite als Bestellkärtchen mit Foto von zukünftigen "Praxisgängern" im Querschnitt. D.h. Zu sehen sein sollten 1 lustige Oma , 1 lustiger Opa (z.B. Pfeife rauchend), 1 Jugendlicher und diverse andere Erwachsene verschiedener Berufsgruppen. Beispielhaft siehe unter: Tintenfuchs: Online Terminvereinbarung-Die keine Wünsche offen lässt. Das Bild könnte auch "gezeichnet" sein. Ich würde aber ein treffendes Foto bevorzugen. Design: gut leserliche Schrift, keine verschlungene Schriftarten, wegen Lesbarkeit für Renterklientel.
Info auf der Vorderseite mit Foto: WARTEN? Nicht bei uns - Ihr persönlicher Wunschtermin:
Info auf der Rückseite (Gutschein): Gutschein für eine Kaffeespezialität (Kaffeesymbol)
farblich unterlegt, Farbe egal, passend abgestimmt zur Vorderseite
Zur Erklärung:
Die Form/ Grösse sollte die einer Visitenkarte möglichst nicht überschreiten. Gern auch eine grössere Visitenkartenform 10cm breit und 7,5 cm hoch. Das Format ist unserem Zeitdruck geschuldet. Es muss ein Werbemittel in 14 Tagen zur Praxiseröffnung zur Verfügung stehen, was sich schnell und kostengünstig produzieren und bei Bedarf ohne Probleme nachproduzieren lässt.
Sonderformate haben lange Auftragszeiten bei den auszuführenden Werbedruckfirmen.

```html
<!DOCTYPE html>
<html lang="de">
<head>
<meta charset="utf-8">
<title>Hausarztpraxis – Terminkarte und Gutschein</title>
<link rel="stylesheet" href="https://fonts.googleapis.com/css2?family=Questrial&display=swap">
<style>
  :root {
    --rose: #c86c6b;
    --navy: #1c4d68;
    --white: #ffffff;
    --page: #ffffff;
    --ink-navy: #1c4d68;
  }
  * { margin: 0; padding: 0; box-sizing: border-box; }
  html, body {
    width: 1200px; height: 1200px; overflow: hidden;
    background: var(--page);
    font-family: "Questrial", "Century Gothic", sans-serif;
  }
  .canvas { position: relative; width: 1200px; height: 1200px; }
  .card {
    position: absolute; left: 217px; width: 774px; height: 500px;
    background: var(--white);
  }
  .card--front { top: 67px; }
  .card--back { top: 603px; height: 501px; }
  .block { position: absolute; }
  .photo { position: absolute; display: block; }

  /* Front */
  .front-rose-top { left: 19px; top: 19px; width: 368px; height: 231px; background: var(--rose); }
  .front-rose-bottom { left: 387px; top: 250px; width: 369px; height: 232px; background: var(--rose); }
  .photo--waiting { left: 387px; top: 19px; width: 369px; height: 231px;
    background: linear-gradient(180deg, #e4e6e4 0%, #d9dbda 45%, #3b3d44 60%, #d7d6d3 85%, #c9c7c3 100%); }
  .photo--seniors { left: 19px; top: 250px; width: 368px; height: 232px;
    background: linear-gradient(160deg, #e8e8e6 0%, #d3d3d0 40%, #b9bcc3 70%, #e9e2d7 100%); }
  .headline-band { left: 0; top: 64px; width: 367px; height: 90px; background: var(--navy); }
  .headline {
    position: absolute; left: 35px; top: 8px;
    color: var(--white); font-size: 70px; line-height: 72px; letter-spacing: 1px;
  }
  .subline {
    position: absolute; left: 33px; top: 160px;
    color: var(--white); font-size: 48px; line-height: 56px;
  }
  .appointment-band { left: 426px; top: 258px; width: 348px; height: 96px; background: var(--navy);
    color: var(--white); font-size: 23px; line-height: 28.5px; padding: 7px 0 0 24px; }
  .appointment-form { left: 426px; top: 363px; width: 330px; height: 109px; background: var(--white);
    color: var(--ink-navy); font-size: 30px; line-height: 50px; padding: 9px 0 0 26px; }

  /* Back */
  .photo--coffee { left: 16px; top: 19px; width: 740px; height: 464px;
    background: radial-gradient(ellipse at 72% 48%, #f1efe9 0%, #e3ddd2 22%, #7a5a42 42%, #4a3326 70%, #3a281f 100%); }
  .voucher-band { left: 0; top: 64px; width: 455px; height: 91px; background: var(--navy); }
  .voucher-title {
    position: absolute; left: 44px; top: 10px;
    color: var(--white); font-size: 72px; line-height: 72px; letter-spacing: 1px;
  }
  .address-box { left: 0; top: 334px; width: 339px; height: 90px; background: var(--rose);
    color: var(--white); font-size: 22px; line-height: 27px; padding: 15px 0 0 36px; }
  .offer-box { left: 426px; top: 364px; width: 348px; height: 108px; background: var(--navy);
    color: var(--white); font-size: 35px; line-height: 44px; padding: 10px 0 0 24px; }
</style>
</head>
<body>
<main class="canvas">

  <section class="card card--front" aria-label="Terminkarte Vorderseite">
    <div class="block front-rose-top"></div>
    <div class="photo photo--waiting" role="img" aria-label="Foto: fünf junge Erwachsene in Businesskleidung sitzen wartend auf Stühlen und schauen auf ihr Handy"></div>
    <div class="photo photo--seniors" role="img" aria-label="Foto: vier fröhliche Senioren zeigen den Daumen nach oben"></div>
    <div class="block front-rose-bottom"></div>
    <div class="block headline-band"><h1 class="headline">WARTEN?</h1></div>
    <p class="subline">Nicht bei uns</p>
    <div class="block appointment-band">Ihr Wunschtermin<br>in der Hausarztpraxis<br>Martin Eschenbach</div>
    <div class="block appointment-form">Datum:<br>Uhrzeit:</div>
  </section>

  <section class="card card--back" aria-label="Gutschein Rückseite">
    <div class="photo photo--coffee" role="img" aria-label="Foto: weiße Espressotasse auf Untertasse mit Amarettini und Kaffeebohnen auf dunklem Holztisch"></div>
    <div class="block voucher-band"><h2 class="voucher-title">GUTSCHEIN</h2></div>
    <div class="block address-box">Martin Eschenbach<br>04299 Wiesenfeld-Birkhain</div>
    <div class="block offer-box">Über eine<br>Kaffespezialität</div>
  </section>

</main>
</body>
</html>
```